Business card for massage therapy company called Brook Fern Wellness

Need business card for massage therapy company called Brook Fern Wellness. Would like my logo on the front and the back of the card I have 3 options of logos and you can play with what looks better.

Would like this information displayed on the back of the card:

Marcus Ellery
Licensed Massage Therapist
321-555-0147
brookfern-example.com
brookfern_rest_

```html
<!DOCTYPE html>
<html lang="en">
<head>
<meta charset="utf-8">
<title>Brook Fern Wellness – Business Card</title>
<link rel="stylesheet" href="https://fonts.googleapis.com/css2?family=Marcellus&family=Arimo:wght@400&display=swap">
<style>
  :root{
    --sage:#7b8070;
    --sage-pale:#dfe1d9;
    --tan:#c99a7c;
    --ink:#55574f;
    --card:#ffffff;
    --backdrop:#e7e6e2;
  }
  *{margin:0;padding:0;box-sizing:border-box}
  html,body{width:1200px;height:886px;overflow:hidden;background:var(--backdrop)}
  .canvas{position:relative;width:1200px;height:886px}
  .card{position:absolute;width:520px;height:297px;background:var(--card);border-radius:24px;overflow:hidden;box-shadow:0 6px 18px rgba(0,0,0,.12)}
  .card--front{left:90px;top:110px}
  .card--back{left:590px;top:470px}
  .card svg.lines{position:absolute;inset:0}

  .brand{position:absolute;display:flex;align-items:center;gap:14px;color:var(--sage);font-family:"Marcellus",serif;text-transform:uppercase;letter-spacing:.12em;line-height:1.05;white-space:nowrap}
  .brand__dot{flex:none;border:2px solid var(--sage);border-radius:50%}
  .card--front .brand{left:120px;top:90px;font-size:24px}
  .card--front .brand__dot{width:64px;height:64px}
  .card--back .brand{left:36px;top:180px;font-size:21px}
  .card--back .brand__dot{width:48px;height:48px}

  .decor-area{position:absolute;left:436px;top:12px;width:68px;height:52px;border-radius:6px;background:var(--sage-pale)}

  .person{position:absolute;left:300px;top:132px;white-space:nowrap}
  .person__name{font-family:"Marcellus",serif;font-size:23px;color:var(--sage);letter-spacing:.04em;line-height:1.1}
  .person__title{font-family:"Arimo",sans-serif;font-size:8.6px;color:var(--tan);letter-spacing:.07em;margin-top:3px}

  .contact{position:absolute;left:300px;top:186px;list-style:none;font-family:"Arimo",sans-serif;color:var(--ink);white-space:nowrap}
  .contact li{display:flex;align-items:center;gap:6px;margin-bottom:5px;font-size:11px;line-height:1.2}
  .contact li.contact__phone{font-size:16px}
  .contact svg{flex:none;width:11px;height:11px;fill:var(--tan)}
</style>
</head>
<body>
<main class="canvas">

  <section class="card card--front" aria-label="Card front">
    <svg class="lines" width="520" height="297" viewBox="0 0 520 297" fill="none">
      <path d="M150 297 C200 200 330 165 520 95" stroke="var(--sage)" stroke-width="1.6"/>
    </svg>
    <div class="brand"><span class="brand__dot"></span><span>Brook Fern<br>Wellness</span></div>
  </section>

  <section class="card card--back" aria-label="Card back">
    <svg class="lines" width="520" height="297" viewBox="0 0 520 297" fill="none">
      <path d="M372 0 C360 80 295 118 165 130" stroke="var(--tan)" stroke-width="1.6"/>
      <path d="M0 215 C40 150 150 150 265 125 C350 106 400 90 430 70" stroke="var(--sage)" stroke-width="1.6"/>
    </svg>
    <div class="decor-area" role="img" aria-label="Place for a small leafy sprig decoration"></div>

    <div class="brand"><span class="brand__dot"></span><span>Brook Fern<br>Wellness</span></div>

    <div class="person">
      <p class="person__name">MARCUS ELLERY</p>
      <p class="person__title">LICENSED MASSAGE THERAPIST</p>
    </div>

    <ul class="contact">
      <li class="contact__phone"><svg viewBox="0 0 24 24"><path d="M6.6 10.8a15.1 15.1 0 0 0 6.6 6.6l2.2-2.2a1 1 0 0 1 1-.25 11.4 11.4 0 0 0 3.6.57 1 1 0 0 1 1 1V20a1 1 0 0 1-1 1A17 17 0 0 1 3 4a1 1 0 0 1 1-1h3.5a1 1 0 0 1 1 1c0 1.25.2 2.45.57 3.57a1 1 0 0 1-.25 1z"/></svg>321-555-0147</li>
      <li><svg viewBox="0 0 24 24"><path d="M2 5h20v14H2zm2 2v.5l8 5 8-5V7z"/></svg>brookfern_rest_@gmail.com</li>
      <li><svg viewBox="0 0 24 24"><circle cx="12" cy="12" r="10"/></svg>www.brookfern-example.com</li>
    </ul>
  </section>

</main>
</body>
</html>
```